Thank You Card design for a federal credit union

I am looking to have a thank you card designed.
Specs:
Flat size of 9.5"x6.5" folds to final size of 4.75"x6.5", it will print full color on the front and back. Below, you will see their logo, which needs to print on the inside of the folded card. I also attached images of their current card. They would like to keep the blue color but are open to design on the front. This is a Federal Credit Union, so please make the design, modern and professional. Below is the text that needs to print below the logo on the inside of the card. The text and logo will print below the fold on the inside, leave the top portion (above the panel) white.
Inside text:
Our Members are the foundation of our Credit Union. We sincerely thank you for your loyalty, your business and the opportunity to serve you.
Target Market(s)
Clients of a federal credit union
Industry/Entity Type
Union
Requirements
Must have
- a simple, professional, and modern feel. "Thank You for your business" must be on the front section in some variation.
Should not have
- nothing flashy or too many colors. keep it simple

```html
<!DOCTYPE html>
<html lang="en">
<head>
<meta charset="utf-8">
<title>Thank You Card – Panel Layout</title>
<link rel="stylesheet" href="https://fonts.googleapis.com/css2?family=PT+Sans:wght@400;700&family=Great+Vibes&family=Almendra:wght@700&display=swap">
<style>
  :root {
    --stage: #e6e7e9;
    --label: #2e3192;
    --panel-white: #ffffff;
    --panel-edge: #3a3a3a;
    --night: #0b0a1b;
    --night-mid: #15143f;
    --leaf-deep: #1d1f7a;
    --ring: #4a58b0;
    --type-blue: #2f86c9;
    --type-script: #43b8e8;
    --ink: #12102e;
  }
  * { margin: 0; padding: 0; box-sizing: border-box; }
  html, body { width: 1200px; height: 800px; overflow: hidden; background: var(--stage); }
  .stage { position: relative; width: 1200px; height: 800px; font-family: "PT Sans", Arial, sans-serif; }

  .label { position: absolute; color: var(--label); font-size: 17px; letter-spacing: 0.2px; }
  .label--outside { left: 279px; top: 34px; }
  .label--inside { left: 864px; top: 34px; }
  .label--back { left: 83px; top: 192px; }
  .label--front { left: 83px; top: 457px; }
  .label--first { left: 1100px; top: 205px; }
  .label--last { left: 1100px; top: 471px; }

  .card { position: absolute; border: 1px solid var(--panel-edge); overflow: hidden; }
  .card--outside { left: 171px; top: 89px; width: 346px; height: 505px; }
  .card--inside { left: 721px; top: 93px; width: 341px; height: 498px; }

  .panel { position: absolute; left: 0; width: 100%; }
  .panel--back { top: 0; height: 252px; background: var(--panel-white); }
  .panel--front {
    top: 252px; height: 252px;
    background: radial-gradient(circle at 50% 50%, var(--night-mid) 0%, #100f2c 45%, var(--night) 75%);
  }
  .panel--first { top: 0; height: 249px; background: var(--panel-white); border-bottom: 1px dashed #c9cad0; }
  .panel--last { top: 249px; height: 249px; background: var(--panel-white); }

  .front-art { position: absolute; left: 0; top: 0; width: 344px; height: 252px; }

  .front-message { position: absolute; left: 0; top: 0; width: 344px; height: 252px; text-align: center; }
  .front-message .line {
    position: absolute; left: 0; width: 100%; color: var(--type-blue);
    text-transform: uppercase; font-weight: 700; white-space: nowrap; line-height: 1;
  }
  .line--lead { top: 84px; font-size: 8px; }
  .line--say { top: 96px; font-size: 10px; }
  .front-message .line--thanks {
    top: 114px; font-family: "Great Vibes", cursive; text-transform: none;
    font-weight: 400; color: var(--type-script); font-size: 28px;
  }
  .line--for { top: 154px; font-size: 10px; }
  .line--business { top: 170px; font-size: 8px; }

  .brand { position: absolute; left: 0; top: 26px; width: 100%; display: flex; justify-content: center; align-items: center; gap: 6px; }
  .brand__mark { width: 13px; height: 13px; background: var(--ink); }
  .brand__name { font-family: "Almendra", serif; font-weight: 700; font-size: 11px; color: var(--ink); }

  .inside-message {
    position: absolute; left: 0; top: 65px; width: 100%; text-align: center; white-space: nowrap;
    font-family: "Almendra", serif; font-weight: 700; font-size: 10px; line-height: 12px;
    letter-spacing: 0.35px; color: var(--ink);
  }
</style>
</head>
<body>
<main class="stage">
  <div class="label label--outside">OUTSIDE</div>
  <div class="label label--inside">INSIDE</div>
  <div class="label label--back">BACK</div>
  <div class="label label--front">FRONT</div>
  <div class="label label--first">FIRST</div>
  <div class="label label--last">LAST</div>

  <section class="card card--outside">
    <div class="panel panel--back"></div>
    <div class="panel panel--front">
      <svg class="front-art" viewBox="0 0 344 252">
        <defs>
          <radialGradient id="leafTone" cx="50%" cy="50%" r="50%">
            <stop offset="0%" stop-color="#232585"/>
            <stop offset="70%" stop-color="#1d1f7a"/>
            <stop offset="100%" stop-color="#3a3fae" stop-opacity="0.45"/>
          </radialGradient>
        </defs>
        <ellipse role="img" aria-label="Cluster of blue autumn leaves framing the message" cx="173" cy="126" rx="113" ry="104" fill="url(#leafTone)"/>
        <circle cx="173" cy="128" r="70" fill="#1b1d70" stroke="var(--ring)" stroke-width="2" stroke-dasharray="5 3"/>
      </svg>
      <div class="front-message">
        <div class="line line--lead">We would</div>
        <div class="line line--say">Like to say</div>
        <div class="line line--thanks">Thank You</div>
        <div class="line line--for">For your</div>
        <div class="line line--business">Business</div>
      </div>
    </div>
  </section>

  <section class="card card--inside">
    <div class="panel panel--first"></div>
    <div class="panel panel--last">
      <div class="brand">
        <span class="brand__mark"></span>
        <span class="brand__name">Ridgeline Federal Credit Union</span>
      </div>
      <p class="inside-message">Our Members are the foundation of our Credit Union. We<br>sincerely thank you for your loyalty, your business and<br>the opportunity to serve you.</p>
    </div>
  </section>
</main>
</body>
</html>
```